Larchmere Hockey Academy

We are are Ice Hockey Development Company that provided on-ice Hockey development services. We need a Landing Page with tabs to direct to individual program pages.
Landing Page
About Page
Winter Program Page
Spring Program Page
Summer Program Page
Team Page
Tournament Page

```html
<!DOCTYPE html>
<html lang="en">
<head>
<meta charset="utf-8">
<title>Larchmere Hockey Academy – Website Pages</title>
<link rel="stylesheet" href="https://fonts.googleapis.com/css2?family=Ubuntu:wght@500;700&family=Montserrat:wght@400;600&display=swap">
<style>
:root{
  --green:#137b13;
  --green-dark:#0e6a0e;
  --black:#000;
  --white:#fff;
  --panel:#f2f2f2;
  --rule:#3a3a3a;
  --text:#222;
  --bg-a:#d9e4d1;
  --bg-b:#d8d9d6;
}
*{box-sizing:border-box;margin:0;padding:0}
html,body{width:1200px;height:1200px;overflow:hidden}
body{background:linear-gradient(160deg,var(--bg-a),var(--bg-b));font-family:"Montserrat",sans-serif;color:var(--text);position:relative}
.abs{position:absolute}
.page{position:absolute;width:347px;background:var(--white);overflow:hidden}

/* brand */
.brand{font-family:"Ubuntu",sans-serif;font-weight:700;color:var(--black);text-transform:uppercase;line-height:1}
.brand-card{left:88px;top:142px;width:252px;height:129px;background:var(--white);display:flex;align-items:center;justify-content:center;gap:10px}
.brand-card .mark{width:18px;height:18px;background:var(--green)}
.brand-card .brand{font-size:26px;letter-spacing:.5px;line-height:1.02}

/* header */
.hdr{position:absolute;left:20px;right:20px;top:8px;height:20px;border-bottom:.8px solid var(--rule);display:flex;align-items:flex-end;justify-content:space-between;padding-bottom:2px}
.hdr .brand{font-size:5.4px;width:44px;line-height:1.05}
.nav{display:flex;gap:7px;font-size:3.1px;letter-spacing:.1px;text-transform:uppercase;padding-bottom:3px}

/* image areas: flat tones only */
.img{position:absolute}
.img-player{background:linear-gradient(180deg,#ececec,#d8d8d8)}
.img-skates{background:linear-gradient(180deg,#d3d9db,#e6eaea)}
.img-mountain{background:linear-gradient(180deg,#d9dde1,#9aa39a)}
.img-rink{background:linear-gradient(180deg,#9a9a9a,#4a4a4a)}
.img-coach{background:linear-gradient(180deg,#8a8a8a,#cfcfcf)}
.img-net{background:linear-gradient(180deg,#b9c7d1,#d6dde2)}

/* text */
.title{font-family:"Ubuntu",sans-serif;font-weight:700;text-transform:uppercase;color:var(--black);font-size:14.5px;line-height:1}
.para{font-size:2.8px;line-height:1.6;color:var(--text)}
.btn{display:inline-flex;align-items:center;justify-content:center;background:var(--green-dark);color:var(--white);font-size:2.6px;text-transform:uppercase;font-weight:600;height:11px;padding:0 8px}

/* cards */
.card{position:absolute;background:var(--panel);text-align:center;display:flex;flex-direction:column;align-items:center;padding-top:8px}
.card h3{font-family:"Ubuntu",sans-serif;font-weight:700;font-size:8px;text-transform:uppercase;color:var(--black)}
.card p{font-size:4px;line-height:1.6;padding:2px 6px 0}
.card .btn{position:absolute;bottom:9px}
.card-photo{background:linear-gradient(180deg,#e9ecee,#d6dbde)}

.band{position:absolute;left:0;right:0;background:var(--green);color:var(--white);font-family:"Ubuntu",sans-serif;font-weight:700;display:flex;align-items:center;justify-content:center;font-size:8.5px}

/* footer */
.ftr{position:absolute;left:0;right:0;height:50px;background:var(--black);color:var(--white)}
.ftr .pill{position:absolute;left:20px;top:13px;width:36px;height:20px;background:var(--white);border-radius:3px;display:flex;align-items:center;justify-content:center}
.ftr .pill .brand{font-size:4px;text-align:center}
.ftr .cols{position:absolute;left:105px;top:13px;display:flex;gap:18px;font-size:2.4px;line-height:1.7;text-transform:uppercase}
.ftr .cols b{display:block;color:#2fa52f;font-weight:400}
.ftr .cols .plain b{color:var(--white)}
.ftr .social{position:absolute;right:20px;top:13px;display:flex;gap:7px}
.ftr .social span{width:7px;height:7px;border:1px solid var(--white);border-radius:1.5px}
.ftr .copy{position:absolute;left:0;right:0;bottom:8px;text-align:center;font-size:2.4px;text-transform:uppercase}

/* contact */
.form{position:absolute;background:var(--panel);padding:8px 10px}
.field{height:11px;border:.6px solid #555;background:var(--white);font-size:2.6px;padding:3px 4px;margin-bottom:6px;text-transform:uppercase}
.pref{display:flex;align-items:center;gap:5px;font-size:2.4px;text-transform:uppercase;margin:1px 0 8px 4px}
.pref .box{width:7px;height:7px;border:.6px solid #555;background:var(--white);margin-right:4px}
.message{height:64px}
.subscribe{position:absolute;left:0;right:0;height:52px;background:linear-gradient(90deg,#2f6e2c,#3f7f3a);color:var(--white)}

/* tournaments */
.tcard{position:absolute;width:73px;height:114px;background:var(--panel);text-align:center}
.tcard .pic{position:absolute;left:6px;top:5px;width:61px;height:60px;background:linear-gradient(180deg,#eeeeee,#d6d6d6)}
.tcard h4{position:absolute;left:0;right:0;top:69px;font-family:"Ubuntu",sans-serif;font-weight:700;font-size:5px;color:var(--green)}
.tcard p{position:absolute;left:0;right:0;top:76px;font-size:2.6px;line-height:1.6;text-transform:uppercase}
.tcard .btn{position:absolute;left:18px;top:96px;padding:0;width:37px}

/* programs */
.dates{position:absolute;left:20px;right:20px;top:130px;height:29px;background:var(--panel)}
.dates .start{position:absolute;left:0;top:0;height:29px;width:170px;background:var(--green);clip-path:polygon(0 0,100% 0,86% 100%,0 100%);color:var(--white);font-family:"Ubuntu",sans-serif;font-weight:700;font-size:8.5px;display:flex;align-items:center;padding-left:17px}
.dates .end{position:absolute;left:192px;top:0;height:29px;display:flex;align-items:center;font-family:"Ubuntu",sans-serif;font-weight:700;font-size:8.5px;color:var(--black)}
.sched-title{position:absolute;left:37px;top:172px;font-family:"Ubuntu",sans-serif;font-weight:700;font-size:6.5px}
.sched{position:absolute;left:20px;right:20px;top:183px;border-collapse:collapse;font-size:4.6px;text-transform:uppercase}
.sched td{height:12.3px;padding-left:17px}
.sched tr:first-child td{border-top:.7px solid var(--rule);border-bottom:.7px solid var(--rule)}
.sched tr:nth-child(odd):not(:first-child) td{background:var(--panel)}
</style>
</head>
<body>

<div class="abs brand-card">
  <span class="mark"></span>
  <div class="brand">Larchmere<br>Hockey<br>Academy</div>
</div>

<!-- Landing page -->
<section class="page" style="left:426px;top:57px;height:376px">
  <header class="hdr"><div class="brand">Larchmere Hockey Academy</div><nav class="nav"><span>About</span><span>Team</span><span>Winter Program</span><span>Spring Program</span><span>Summer Program</span><span>Tournaments</span></nav></header>
  <div class="img img-player" style="left:20px;top:37px;width:184px;height:133px" role="img" aria-label="Photo of a hockey player taking a shot"></div>
  <h1 class="title abs" style="left:217px;top:60px">Lorem Ipsom</h1>
  <p class="para abs" style="left:217px;top:80px;width:110px">Our coaches build skating, puck control and game sense through focused on-ice sessions. Players of every level train in small groups, get clear feedback and leave each week with skills they can use in their next game. We keep numbers low so every athlete gets real ice time and attention from staff who know the game and love to teach it each season.</p>
  <span class="btn abs" style="left:217px;top:139px;width:36px;padding:0">Learn More</span>
  <div class="band" style="top:181px;height:28px">We offer programs in Winter, Spring, and Summer!</div>
  <div class="card card-photo" style="left:56px;top:220px;width:72px;height:96px" role="img" aria-label="Winter program card with an ice photo behind"><h3>Winter</h3><p>Small group ice sessions built for skill, speed and confidence.</p><span class="btn">Learn More</span></div>
  <div class="card card-photo" style="left:137px;top:220px;width:72px;height:96px" role="img" aria-label="Spring program card with an ice photo behind"><h3>Spring</h3><p>Small group ice sessions built for skill, speed and confidence.</p><span class="btn">Learn More</span></div>
  <div class="card card-photo" style="left:218px;top:220px;width:72px;height:96px" role="img" aria-label="Summer program card with an ice photo behind"><h3>Summer</h3><p>Small group ice sessions built for skill, speed and confidence.</p><span class="btn">Learn More</span></div>
  <footer class="ftr" style="top:326px"><div class="pill"><div class="brand">Larchmere<br>Hockey</div></div><div class="cols"><div><b>Who We Are</b>About<br>Team<br>Tournaments<br>Alumni</div><div><b>Programs</b>Winter<br>Spring<br>Summer</div><div><b>Contact Us</b></div></div><div class="social"><span></span><span></span></div><div class="copy">Copyright 2023</div></footer>
</section>

<!-- About page -->
<section class="page" style="left:813px;top:57px;height:247px">
  <header class="hdr"><div class="brand">Larchmere Hockey Academy</div><nav class="nav"><span>About</span><span>Team</span><span>Winter Program</span><span>Spring Program</span><span>Summer Program</span><span>Tournaments</span></nav></header>
  <div class="img img-skates" style="left:20px;top:37px;width:124px;height:142px" role="img" aria-label="Photo of old hockey skates in the snow"></div>
  <h1 class="title abs" style="left:158px;top:50px">About Us</h1>
  <p class="para abs" style="left:158px;top:70px;width:170px">Our coaches build skating, puck control and game sense through focused on-ice sessions. Players of every level train in small groups, get clear feedback and leave each week with skills they can use in their next game. We keep numbers low so every athlete gets real ice time and attention from staff who know the game and love to teach it.<br><br>From first strides to high level play, our programs grow with each player. Families can count on safe, well run sessions, honest progress notes and a friendly rink culture.</p>
  <span class="btn abs" style="left:158px;top:154px;width:36px;padding:0">Contact Us</span>
  <footer class="ftr" style="top:197px"><div class="pill"><div class="brand">Larchmere<br>Hockey</div></div><div class="cols"><div><b>Who We Are</b>About<br>Team<br>Tournaments</div><div><b>Programs</b>Winter<br>Spring<br>Summer</div><div class="plain"><b>Contact Us</b></div></div><div class="social"><span></span><span></span></div><div class="copy">Copyright 2023</div></footer>
</section>

<!-- Contact page -->
<section class="page" style="left:40px;top:421px;height:337px">
  <header class="hdr"><div class="brand">Larchmere Hockey Academy</div><nav class="nav"><span>About</span><span>Team</span><span>Winter Program</span><span>Spring Program</span><span>Summer Program</span><span>Tournaments</span></nav></header>
  <div class="img img-mountain" style="left:20px;top:37px;width:113px;height:184px" role="img" aria-label="Photo of players skating on a frozen lake below a mountain"></div>
  <h1 class="title abs" style="left:144px;top:40px">Contact Us</h1>
  <form class="form" style="left:144px;top:62px;width:188px;height:159px">
    <div class="field">Name</div><div class="field">Email</div><div class="field">Phone</div>
    <div class="pref"><span style="flex:1">Preferred method of contact:</span>Text<span class="box"></span>Phone<span class="box"></span>Email<span class="box"></span></div>
    <div class="field message">Message</div>
    <span class="btn abs" style="left:76px;top:142px;width:36px;padding:0">Send</span>
  </form>
  <div class="subscribe" style="top:235px" role="img" aria-label="Green tinted photo of a hockey team on the bench">
    <div class="abs" style="left:25px;top:8px;font-family:'Ubuntu',sans-serif;font-weight:700;font-size:13px">SUBSCRIBE</div>
    <div class="abs" style="left:153px;top:14px;font-size:5.8px">Stay up to date on events and alumni news!</div>
    <div class="abs" style="left:53px;top:27px;width:166px;height:10px;background:var(--white);color:var(--text);font-size:2.6px;padding:3px 4px">EMAIL ADDRESS</div>
    <span class="btn abs" style="left:228px;top:27px;height:10px;width:35px;padding:0;background:#111">Sign Up</span>
  </div>
  <footer class="ftr" style="top:287px"><div class="pill"><div class="brand">Larchmere<br>Hockey</div></div><div class="cols"><div><b>Who We Are</b>About<br>Team<br>Tournaments</div><div><b>Programs</b>Winter<br>Spring<br>Summer</div><div class="plain"><b>Contact Us</b></div></div><div class="social"><span></span><span></span></div><div class="copy">Copyright 2023</div></footer>
</section>

<!-- Team page -->
<section class="page" style="left:426px;top:475px;height:282px">
  <header class="hdr"><div class="brand">Larchmere Hockey Academy</div><nav class="nav"><span>About</span><span>Team</span><span>Winter Program</span><span>Spring Program</span><span>Summer Program</span><span>Tournaments</span></nav></header>
  <div class="img img-coach" style="left:20px;top:37px;width:121px;height:87px" role="img" aria-label="Black and white photo of a coach with players on the ice"></div>
  <h1 class="title abs" style="left:157px;top:40px">Our Team</h1>
  <p class="para abs" style="left:157px;top:60px;width:170px">Our coaches build skating, puck control and game sense through focused on-ice sessions. Players of every level train in small groups, get clear feedback and leave each week with skills they can use in their next game. We keep numbers low so every athlete gets real ice time and attention from staff who know the game and love to teach it. From first strides to high level play, our programs grow with each player and families can count on safe, well run sessions.</p>
  <div class="card" style="left:60px;top:136px;width:72px;height:85px"><h3>Team</h3><p>Small group ice sessions built for skill, speed and confidence.</p><span class="btn">Learn More</span></div>
  <div class="card" style="left:141px;top:136px;width:72px;height:85px"><h3>Team</h3><p>Small group ice sessions built for skill, speed and confidence.</p><span class="btn">Learn More</span></div>
  <div class="card" style="left:222px;top:136px;width:72px;height:85px"><h3>Team</h3><p>Small group ice sessions built for skill, speed and confidence.</p><span class="btn">Learn More</span></div>
  <footer class="ftr" style="top:232px"><div class="pill"><div class="brand">Larchmere<br>Hockey</div></div><div class="cols"><div><b>Who We Are</b>About<br>Team<br>Tournaments</div><div><b>Programs</b>Winter<br>Spring<br>Summer</div><div class="plain"><b>Contact Us</b></div></div><div class="social"><span></span><span></span></div><div class="copy">Copyright 2023</div></footer>
</section>

<!-- Tournaments page -->
<section class="page" style="left:812px;top:325px;height:433px">
  <header class="hdr"><div class="brand">Larchmere Hockey Academy</div><nav class="nav"><span>About</span><span>Team</span><span>Winter Program</span><span>Spring Program</span><span>Summer Program</span><span>Tournaments</span></nav></header>
  <div class="img img-rink" style="left:20px;top:37px;width:121px;height:87px" role="img" aria-label="Black and white photo of players on a bench beside the rink"></div>
  <h1 class="title abs" style="left:157px;top:40px">Tournaments</h1>
  <p class="para abs" style="left:157px;top:62px;width:170px">Our coaches build skating, puck control and game sense through focused on-ice sessions. Players of every level train in small groups, get clear feedback and leave each week with skills they can use in their next game. We keep numbers low so every athlete gets real ice time and attention from staff who know the game and love to teach it. From first strides to high level play, our programs grow with each player and families can count on safe, well run sessions.</p>
  <div class="tcard" style="left:57px;top:132px"><div class="pic" role="img" aria-label="Photo of a hockey player shooting"></div><h4>TOURNAMENT</h4><p>Dates<br>Location</p><span class="btn">Learn More</span></div>
  <div class="tcard" style="left:138px;top:132px"><div class="pic" role="img" aria-label="Photo of a hockey player shooting"></div><h4>TOURNAMENT</h4><p>Dates<br>Location</p><span class="btn">Learn More</span></div>
  <div class="tcard" style="left:219px;top:132px"><div class="pic" role="img" aria-label="Photo of a hockey player shooting"></div><h4>TOURNAMENT</h4><p>Dates<br>Location</p><span class="btn">Learn More</span></div>
  <div class="tcard" style="left:57px;top:257px"><div class="pic" role="img" aria-label="Photo of a hockey player shooting"></div><h4>TOURNAMENT</h4><p>Dates<br>Location</p><span class="btn">Learn More</span></div>
  <div class="tcard" style="left:138px;top:257px"><div class="pic" role="img" aria-label="Photo of a hockey player shooting"></div><h4>TOURNAMENT</h4><p>Dates<br>Location</p><span class="btn">Learn More</span></div>
  <div class="tcard" style="left:219px;top:257px"><div class="pic" role="img" aria-label="Photo of a hockey player shooting"></div><h4>TOURNAMENT</h4><p>Dates<br>Location</p><span class="btn">Learn More</span></div>
  <footer class="ftr" style="top:383px"><div class="pill"><div class="brand">Larchmere<br>Hockey</div></div><div class="cols"><div><b>Who We Are</b>About<br>Team<br>Tournaments</div><div><b>Programs</b>Winter<br>Spring<br>Summer</div><div class="plain"><b>Contact Us</b></div></div><div class="social"><span></span><span></span></div><div class="copy">Copyright 2023</div></footer>
</section>

<!-- Winter program -->
<section class="page" style="left:40px;top:801px;height:342px">
  <header class="hdr"><div class="brand">Larchmere Hockey Academy</div><nav class="nav"><span>About</span><span>Team</span><span>Winter Program</span><span>Spring Program</span><span>Summer Program</span><span>Tournaments</span></nav></header>
  <div class="img img-net" style="left:20px;top:36px;width:121px;height:87px" role="img" aria-label="Photo of a hockey net on an outdoor frozen pond"></div>
  <h1 class="title abs" style="left:157px;top:40px">Winter Program</h1>
  <p class="para abs" style="left:157px;top:63px;width:170px">Our coaches build skating, puck control and game sense through focused on-ice sessions. Players of every level train in small groups, get clear feedback and leave each week with skills they can use in their next game. We keep numbers low so every athlete gets real ice time and attention from staff who know the game and love to teach it. From first strides to high level play, our programs grow with each player.</p>
  <div class="dates"><div class="start">STARTS NOV 1ST</div><div class="end">ENDS MARCH 1ST</div></div>
  <div class="sched-title">SCHEDULE</div>
  <table class="sched" style="width:307px"><tr><td>Team</td><td>Date</td><td>Time</td></tr><tr><td>Team</td><td>Date</td><td>Time</td></tr><tr><td>Team</td><td>Date</td><td>Time</td></tr><tr><td>Team</td><td>Date</td><td>Time</td></tr><tr><td>Team</td><td>Date</td><td>Time</td></tr><tr><td>Team</td><td>Date</td><td>Time</td></tr><tr><td>Team</td><td>Date</td><td>Time</td></tr><tr><td>Team</td><td>Date</td><td>Time</td></tr></table>
  <footer class="ftr" style="top:292px"><div class="pill"><div class="brand">Larchmere<br>Hockey</div></div><div class="cols"><div><b>Who We Are</b>About<br>Team<br>Tournaments</div><div><b>Programs</b>Winter<br>Spring<br>Summer</div><div class="plain"><b>Contact Us</b></div></div><div class="social"><span></span><span></span></div><div class="copy">Copyright 2023</div></footer>
</section>

<!-- Spring program -->
<section class="page" style="left:426px;top:801px;height:342px">
  <header class="hdr"><div class="brand">Larchmere Hockey Academy</div><nav class="nav"><span>About</span><span>Team</span><span>Winter Program</span><span>Spring Program</span><span>Summer Program</span><span>Tournaments</span></nav></header>
  <div class="img img-net" style="left:20px;top:36px;width:121px;height:87px" role="img" aria-label="Photo of a hockey net on an outdoor frozen pond"></div>
  <h1 class="title abs" style="left:157px;top:40px">Spring Program</h1>
  <p class="para abs" style="left:157px;top:63px;width:170px">Our coaches build skating, puck control and game sense through focused on-ice sessions. Players of every level train in small groups, get clear feedback and leave each week with skills they can use in their next game. We keep numbers low so every athlete gets real ice time and attention from staff who know the game and love to teach it. From first strides to high level play, our programs grow with each player.</p>
  <div class="dates"><div class="start">STARTS FEB 1ST</div><div class="end">ENDS JUNE 1ST</div></div>
  <div class="sched-title">SCHEDULE</div>
  <table class="sched" style="width:307px"><tr><td>Team</td><td>Date</td><td>Time</td></tr><tr><td>Team</td><td>Date</td><td>Time</td></tr><tr><td>Team</td><td>Date</td><td>Time</td></tr><tr><td>Team</td><td>Date</td><td>Time</td></tr><tr><td>Team</td><td>Date</td><td>Time</td></tr><tr><td>Team</td><td>Date</td><td>Time</td></tr><tr><td>Team</td><td>Date</td><td>Time</td></tr><tr><td>Team</td><td>Date</td><td>Time</td></tr></table>
  <footer class="ftr" style="top:292px"><div class="pill"><div class="brand">Larchmere<br>Hockey</div></div><div class="cols"><div><b>Who We Are</b>About<br>Team<br>Tournaments</div><div><b>Programs</b>Winter<br>Spring<br>Summer</div><div class="plain"><b>Contact Us</b></div></div><div class="social"><span></span><span></span></div><div class="copy">Copyright 2023</div></footer>
</section>

<!-- Summer program -->
<section class="page" style="left:813px;top:801px;height:342px">
  <header class="hdr"><div class="brand">Larchmere Hockey Academy</div><nav class="nav"><span>About</span><span>Team</span><span>Winter Program</span><span>Spring Program</span><span>Summer Program</span><span>Tournaments</span></nav></header>
  <div class="img img-net" style="left:20px;top:36px;width:121px;height:87px" role="img" aria-label="Photo of a hockey net on an outdoor frozen pond"></div>
  <h1 class="title abs" style="left:157px;top:40px">Summer Program</h1>
  <p class="para abs" style="left:157px;top:63px;width:170px">Our coaches build skating, puck control and game sense through focused on-ice sessions. Players of every level train in small groups, get clear feedback and leave each week with skills they can use in their next game. We keep numbers low so every athlete gets real ice time and attention from staff who know the game and love to teach it. From first strides to high level play, our programs grow with each player.</p>
  <div class="dates"><div class="start">STARTS MAY 1ST</div><div class="end">ENDS SEPT 1ST</div></div>
  <div class="sched-title">SCHEDULE</div>
  <table class="sched" style="width:307px"><tr><td>Team</td><td>Date</td><td>Time</td></tr><tr><td>Team</td><td>Date</td><td>Time</td></tr><tr><td>Team</td><td>Date</td><td>Time</td></tr><tr><td>Team</td><td>Date</td><td>Time</td></tr><tr><td>Team</td><td>Date</td><td>Time</td></tr><tr><td>Team</td><td>Date</td><td>Time</td></tr><tr><td>Team</td><td>Date</td><td>Time</td></tr><tr><td>Team</td><td>Date</td><td>Time</td></tr></table>
  <footer class="ftr" style="top:292px"><div class="pill"><div class="brand">Larchmere<br>Hockey</div></div><div class="cols"><div><b>Who We Are</b>About<br>Team<br>Tournaments</div><div><b>Programs</b>Winter<br>Spring<br>Summer</div><div class="plain"><b>Contact Us</b></div></div><div class="social"><span></span><span></span></div><div class="copy">Copyright 2023</div></footer>
</section>

</body>
</html>
```